Business Card for Start-Up Consulting Business
TK Advisory Partners, LLC
Business Card for Start-Up Consulting Business - Consulting
Creative Brief
Professional
Roderick Lyle Pemberton
President/CEO
82 Fenwhistle Court #2410 Dover, DE 19906
info@tkapllc.example
www.tkapllc.example
On the back of the card, I would like something like: Text TKTEAM to 38217 for updates and promotions or For updates and promotions, text TKTEAM to 38217. I would also like to have our services listed on the back of the card like: We Specialize In: or Our Services Includes: *Negative Equity Financing *Tax Mitigation *Life & Health Insurance *Merchant Processing *Telecommunications *Energy Saving Programs *Marketing & Advertising and *More. And if the back is not crowded, maybe we can added the phone, fax, email and/or web address. Thanks

```html
<!DOCTYPE html>
<html lang="en">
<head>
<meta charset="utf-8">
<title>TK Advisory Partners, LLC — Stationery Concepts</title>
<link href="https://fonts.googleapis.com/css2?family=Open+Sans:wght@400;600;700&display=swap" rel="stylesheet">
<style>
  :root{
    --backdrop:#3b2d23;
    --paper:#ffffff;
    --paper-shade:#f1f3f5;
    --brand-blue:#1f4e8c;
    --brand-blue-deep:#173d70;
    --brand-green:#5aa833;
    --ink:#4a5563;
    --label:#cbbfb2;
    --ghost:#d9dee6;
  }
  *{box-sizing:border-box;margin:0;padding:0}
  html,body{width:1200px;height:466px;overflow:hidden;background:var(--backdrop)}
  body{font-family:"Open Sans",Arial,sans-serif;position:relative}
  .piece{position:absolute;background:var(--paper);box-shadow:0 2px 6px rgba(0,0,0,.35);overflow:hidden}
  .label{position:absolute;font-size:6px;letter-spacing:.12em;color:var(--label);text-transform:uppercase}
  .wave{position:absolute;left:0;bottom:0;width:100%;display:block}
  .brand{display:flex;align-items:center;gap:4px}
  .brand-mark{width:10px;height:10px;background:var(--brand-green);flex:none}
  .brand-name{color:var(--brand-blue);font-weight:600;white-space:nowrap}

  /* business cards */
  .card{left:24px;width:82px;height:48px}
  .card-front{top:233px}
  .card-back{top:318px}
  .card .brand{position:absolute;left:5px;top:8px}
  .card .brand-mark{width:6px;height:6px}
  .card .brand-name{font-size:4px}
  .card-front .details{position:absolute;left:5px;top:19px;font-size:2.6px;line-height:1.45;color:var(--ink)}
  .card-back .brand{left:50%;top:14px;transform:translateX(-50%)}
  .card-back .promo{position:absolute;left:0;right:0;top:24px;text-align:center;font-size:2.6px;color:var(--ink)}

  /* letterheads */
  .letterhead{top:30px;width:355px;height:412px}
  .letterhead-one{left:125px}
  .letterhead-two{left:492px}
  .letterhead .brand{position:absolute;left:20px;top:18px}
  .letterhead .brand-name{font-size:8px}
  .letterhead .contact{position:absolute;right:22px;top:16px;font-size:4.2px;line-height:1.6;color:var(--ink)}
  .letterhead .contact li{list-style:none;display:flex;align-items:center;gap:3px}
  .letterhead .contact li::before{content:"";width:3px;height:3px;background:var(--brand-blue)}
  .letterhead-two .brand{left:50%;transform:translateX(-50%)}
  .ghost-name{position:absolute;left:0;right:0;top:120px;text-align:center;font-size:44px;font-weight:700;color:var(--ghost);letter-spacing:.04em}
  .footer-line{position:absolute;left:0;right:0;bottom:26px;text-align:center;font-size:4.2px;color:var(--ink);z-index:2}

  /* envelopes */
  .envelope{left:869px;width:307px}
  .envelope-flap{top:30px;height:132px;background:var(--brand-blue)}
  .envelope-flap .inner{position:absolute;left:0;right:0;top:62px;bottom:0;background:var(--brand-green)}
  .envelope-back{top:168px;height:128px;background:var(--paper-shade)}
  .envelope-back .brand{position:absolute;left:50%;top:40px;transform:translateX(-50%)}
  .envelope-back .brand-name{font-size:6px}
  .envelope-front{top:300px;height:142px}
  .envelope-front .brand{position:absolute;left:14px;top:12px}
  .envelope-front .brand-name{font-size:6px}
  .envelope-front .return{position:absolute;left:14px;top:26px;font-size:3.6px;color:var(--ink)}
</style>
</head>
<body>
  <p class="label" style="left:24px;top:168px">Stationery Concepts</p>

  <section class="piece card card-front" aria-label="Business card front">
    <div class="brand"><span class="brand-mark"></span><span class="brand-name">TK Advisory Partners, LLC</span></div>
    <div class="details">
      <p><strong>Roderick Lyle Pemberton</strong> · President/CEO</p>
      <p>82 Fenwhistle Court #2410 Dover, DE 19906</p>
      <p>info@tkapllc.example · www.tkapllc.example</p>
    </div>
    <svg class="wave" viewBox="0 0 100 14" preserveAspectRatio="none" height="9"><path d="M0 6 C30 0 60 12 100 3 V14 H0Z" fill="var(--brand-green)"/><path d="M0 9 C30 3 60 14 100 6 V14 H0Z" fill="var(--brand-blue)"/></svg>
  </section>
  <p class="label" style="left:24px;top:285px">Business Card Front</p>

  <section class="piece card card-back" aria-label="Business card back">
    <div class="brand"><span class="brand-mark"></span><span class="brand-name">TK Advisory Partners, LLC</span></div>
    <p class="promo">Text TKTEAM to 38217 for updates</p>
  </section>
  <p class="label" style="left:24px;top:370px">Business Card Back</p>

  <section class="piece letterhead letterhead-one" aria-label="Letterhead option 1">
    <div class="brand"><span class="brand-mark"></span><span class="brand-name">TK Advisory Partners, LLC</span></div>
    <ul class="contact">
      <li>82 Fenwhistle Court #2410 Dover, DE 19906</li>
      <li>Phone (302) 555-0148</li>
      <li>Fax (302) 555-0149</li>
      <li>info@tkapllc.example</li>
      <li>www.tkapllc.example</li>
    </ul>
    <svg class="wave" viewBox="0 0 360 44" preserveAspectRatio="none" height="40"><path d="M0 14 C110 0 230 34 360 8 V44 H0Z" fill="var(--brand-green)"/><path d="M0 22 C110 6 230 42 360 16 V44 H0Z" fill="var(--brand-blue)"/></svg>
  </section>
  <p class="label" style="left:262px;top:450px">Letterhead Option 1</p>

  <section class="piece letterhead letterhead-two" aria-label="Letterhead option 2">
    <div class="brand"><span class="brand-mark"></span><span class="brand-name">TK Advisory Partners, LLC</span></div>
    <p class="ghost-name">TK Advisory Partners</p>
    <p class="footer-line">82 Fenwhistle Court #2410 Dover, DE 19906 · (302) 555-0148 · info@tkapllc.example · www.tkapllc.example</p>
    <svg class="wave" viewBox="0 0 360 44" preserveAspectRatio="none" height="40"><path d="M0 14 C110 0 230 34 360 8 V44 H0Z" fill="var(--brand-green)"/><path d="M0 22 C110 6 230 42 360 16 V44 H0Z" fill="var(--brand-blue)"/></svg>
  </section>
  <p class="label" style="left:629px;top:450px">Letterhead Option 2</p>

  <section class="piece envelope envelope-flap" aria-label="Envelope flap">
    <div class="inner"></div>
  </section>

  <section class="piece envelope envelope-back" aria-label="Envelope back">
    <div class="brand"><span class="brand-mark"></span><span class="brand-name">TK Advisory Partners, LLC</span></div>
  </section>

  <section class="piece envelope envelope-front" aria-label="Envelope front">
    <div class="brand"><span class="brand-mark"></span><span class="brand-name">TK Advisory Partners, LLC</span></div>
    <p class="return">82 Fenwhistle Court #2410 Dover, DE 19906</p>
    <svg class="wave" viewBox="0 0 360 44" preserveAspectRatio="none" height="30"><path d="M0 14 C110 0 230 34 360 8 V44 H0Z" fill="var(--brand-green)"/><path d="M0 22 C110 6 230 42 360 16 V44 H0Z" fill="var(--brand-blue)"/></svg>
  </section>
  <p class="label" style="left:990px;top:450px">Envelope Option 1</p>
</body>
</html>
```